Financial Planning business needs a Web Design

Web design needed for financial planning business that encompasses investments, insurance and corporate planning. Would like a sleek, simple design that includes elements of nature/trees and lifestyle based imagery, with an overall feel of trustworthiness, security, growth and freedom. We like the layout of www.quillmerrowfinancial.example, tovafinancial.example and pemlorvane.example, but with more color and images consistent with the nature/lifestyle theme.
Updates

Target Market(s)

New and existing clients

Industry/Entity Type

Financial

Number of Pages Required

5+ page

Requirements
Nice to have
• link to twitter feed
• 'latest features' link to articles
• links to action - buy insurance, get a quote, etc/

```html
<!DOCTYPE html>
<html lang="en">
<head>
<meta charset="utf-8">
<title>Larchmere Wealth Planning</title>
<link href="https://fonts.googleapis.com/css2?family=Open+Sans:wght@400;600;700&display=swap" rel="stylesheet">
<style>
:root{
  --green:#3f9d2b;
  --green-dark:#2f7f1f;
  --green-light:#d8f3b6;
  --text:#555;
  --heading:#444;
  --rule:#e2e2e2;
  --footer:#e8e8e8;
  --bottom:#585858;
  --white:#fff;
}
*{box-sizing:border-box;margin:0;padding:0}
html,body{width:747px;height:1200px;overflow:hidden;background:var(--white);font-family:"Open Sans",sans-serif;color:var(--text)}
.page{position:relative;width:747px;height:1200px}
.abs{position:absolute}

.brand{left:62px;top:30px;display:flex;align-items:center;gap:10px}
.brand-mark{width:30px;height:30px;background:var(--green)}
.brand-name{font-size:20px;font-weight:600;color:var(--green-dark);line-height:1.1}

.nav{left:0;top:94px;width:747px;height:29px;background:var(--green-light)}
.nav a{position:absolute;top:0;height:29px;line-height:29px;font-size:8.5px;color:#333;text-decoration:none;text-align:center;text-transform:uppercase}
.nav a.active{background:var(--green);color:var(--white)}
.nav .sep{position:absolute;top:0;width:1px;height:29px;background:#c3e39c}

.hero{left:0;top:123px;width:747px;height:266px;background:linear-gradient(100deg,#6f5a2a 0%,#a88a2e 30%,#c9a431 55%,#8f8a2a 80%,#5d6d22 100%)}
.hero-title{left:413px;top:177px;width:290px;font-size:23px;font-weight:700;line-height:35px;color:var(--white);letter-spacing:.3px}
.hero-text{left:414px;top:255px;width:255px;font-size:8px;line-height:16px;color:var(--white)}
.btn{display:block;background:var(--green);color:var(--white);font-weight:600;text-align:center;border:2px solid #5fc047}
.hero-btn{left:414px;top:316px;width:120px;height:29px;line-height:25px;font-size:13px}
.arrow{top:242px}

h2{font-weight:400;color:var(--heading)}
.about-h{left:62px;top:412px;font-size:17px}
.about-img{left:62px;top:447px;width:100px;height:88px;background:linear-gradient(135deg,#ddd,#7b7b7b 60%,#333)}
.about-text{left:179px;top:450px;width:460px;font-size:7.6px;line-height:17px}
.more{color:var(--green);font-weight:700;font-size:7.6px}
.about-more{left:181px;top:520px}
.rule{left:62px;width:624px;height:1px;background:var(--rule)}

.latest-h{left:62px;top:576px;font-size:17px}
.pager{top:578px;width:19px;height:19px;background:#dcdcdc}
.card{top:622px;width:142px}
.card-img{height:103px}
.card h3{margin-top:11px;font-size:10.5px;font-weight:600;color:#444}
.meta{margin-top:4px;font-size:6.5px;color:#777;display:flex;gap:6px;align-items:center}
.card p{margin-top:8px;font-size:7.6px;line-height:14px}

.ins-h{left:62px;top:834px;font-size:17px}
.ins-text{left:63px;top:867px;width:380px;font-size:7.6px;line-height:17px}
.ins-btn{left:63px;top:930px;width:96px;height:24px;line-height:20px;font-size:10.5px}

.quote{left:509px;top:832px;width:174px;height:134px;border:1px solid #ddd;background:var(--white)}
.quote-h{height:30px;background:var(--green);color:var(--white);font-size:15px;font-weight:600;text-align:center;line-height:30px}
.quote p{margin:8px 13px 0;font-size:8px;line-height:13.5px;color:#444}
.quote .field{margin:8px 0 0 13px;width:149px;height:22px;border:1px solid #ccc;font-size:7px;color:#999;line-height:20px;padding-left:12px}
.quote-btn{margin:9px 0 0 44px;width:89px;height:24px;line-height:20px;font-size:9.5px}

.footer{left:0;top:983px;width:747px;height:177px;background:var(--footer)}
.col-rule{top:1003px;width:1px;height:135px;background:#d4d4d4}
.f-h{top:1011px;font-size:9.5px;color:#333;text-transform:uppercase;display:flex;align-items:center;gap:6px}
.f-list{list-style:none;font-size:7.4px;color:#444}
.f-list li{height:19.5px}
.f-links{left:64px;top:1038px}
.f-links li{height:19.6px}
.f-res{left:425px;top:1036px;color:#666}
.f-res li{height:15.8px}
.tweet{left:195px;top:1037px;width:172px;height:95px;background:var(--white);border:1px solid #ddd}
.avatar{left:6px;top:6px;width:34px;height:30px;background:linear-gradient(#cfd4da,#6a6f77)}
.tw-text{left:55px;top:7px;width:115px;font-size:7.1px;line-height:13px;color:#333}
.tw-text b{font-weight:600}
.tw-text i,.tw-handle{color:var(--green)}
.tw-actions{left:22px;top:78px;display:flex;gap:15px}
.tw-summary{right:10px;top:78px;font-size:7.4px;color:#d33;text-decoration:underline}
.contact{left:579px;font-size:7.4px;line-height:13.5px;color:#444}
.contact-row{display:flex;gap:8px;position:absolute;left:579px}

.bottom{left:0;top:1160px;width:747px;height:40px;background:var(--bottom)}
.copy{left:0;width:747px;top:1174px;text-align:center;font-size:7.4px;color:#ddd}
.social{top:1169px;width:16px;height:16px;background:#999}
</style>
</head>
<body>
<div class="page">

  <div class="abs brand">
    <span class="brand-mark"></span>
    <span class="brand-name">Larchmere Wealth Planning</span>
  </div>

  <nav class="abs nav">
    <a class="active" style="left:62px;width:60px">Home</a>
    <a style="left:122px;width:94px">About Us</a>
    <span class="sep" style="left:216px"></span>
    <a style="left:216px;width:101px">What We Do</a>
    <span class="sep" style="left:317px"></span>
    <a style="left:317px;width:139px">Interesting Articles</a>
    <span class="sep" style="left:456px"></span>
    <a style="left:456px;width:89px">Our Team</a>
    <span class="sep" style="left:545px"></span>
    <a style="left:545px;width:86px">Contact</a>
    <span class="sep" style="left:631px"></span>
    <svg class="abs" style="left:653px;top:8px" width="13" height="13" viewBox="0 0 13 13"><circle cx="5.2" cy="5.2" r="3.8" fill="none" stroke="#3f9d2b" stroke-width="2"/><line x1="8" y1="8" x2="12" y2="12" stroke="#3f9d2b" stroke-width="2.4" stroke-linecap="round"/></svg>
  </nav>

  <div class="abs hero" role="img" aria-label="Mother hugging her smiling child outdoors among autumn leaves"></div>
  <svg class="abs arrow" style="left:14px" width="14" height="26" viewBox="0 0 14 26"><polyline points="12,2 2,13 12,24" fill="none" stroke="#fff" stroke-width="2.6"/></svg>
  <svg class="abs arrow" style="left:708px" width="14" height="26" viewBox="0 0 14 26"><polyline points="2,2 12,13 2,24" fill="none" stroke="#fff" stroke-width="2.6"/></svg>
  <h1 class="abs hero-title">LARCHMERE WEALTH PLANNING</h1>
  <p class="abs hero-text">At vero eos et accusamus et iusto odio dignissimos ducimus qui blanditiis praesentium voluptatum deleniti atque corrupti quos accusamus dolores ...</p>
  <a class="abs btn hero-btn">GET A QUOTE</a>

  <h2 class="abs about-h">About Larchmere Wealth planning</h2>
  <div class="abs about-img" role="img" aria-label="Smiling businesswoman in an office with colleagues behind her"></div>
  <p class="abs about-text">Lorem Ipsum is simply dummy text of the printing and typesetting industry. Lorem Ipsum has been the industry's standard dummy text ever since the 1500s, when an unknown printer took a galley of type and scrambled it to make a type specimen book. It has survived not only five centuries Lorem Ipsum is simply dummy text of the printing and typesetting industry. Lorem Ipsum has been the industry's standard dummy text ever since the 1500s .</p>
  <span class="abs more about-more">Read More »</span>
  <div class="abs rule" style="top:559px"></div>

  <h2 class="abs latest-h">Latest Articles</h2>
  <div class="abs pager" style="left:644px"><svg width="19" height="19" viewBox="0 0 19 19"><polyline points="11,5 7,9.5 11,14" fill="none" stroke="#555" stroke-width="1.4"/></svg></div>
  <div class="abs pager" style="left:665px"><svg width="19" height="19" viewBox="0 0 19 19"><polyline points="8,5 12,9.5 8,14" fill="none" stroke="#555" stroke-width="1.4"/></svg></div>

  <div class="abs card" style="left:62px">
    <div class="card-img" role="img" aria-label="Hands reviewing financial charts on a desk with a tablet" style="background:linear-gradient(135deg,#3a3f4a,#c9d3e0 55%,#3d6fb4)"></div>
    <h3>Bonorum et Malorum</h3>
    <div class="meta"><span>▦ 04/05/2015</span><span>◷ 9.00 am</span><span>◌ 20</span></div>
    <p>Contrary to popular Ipsum simply random ... <span class="more">Read More »</span></p>
  </div>
  <div class="abs card" style="left:222px">
    <div class="card-img" role="img" aria-label="Business team meeting around a laptop in a bright office" style="background:linear-gradient(135deg,#d9dde2,#8f949b 50%,#2f3238)"></div>
    <h3>Bonorum et Malorum</h3>
    <div class="meta"><span>▦ 04/05/2015</span><span>◷ 9.00 am</span><span>◌ 20</span></div>
    <p>Contrary to popular Ipsum simply random ... <span class="more">Read More »</span></p>
  </div>
  <div class="abs card" style="left:383px">
    <div class="card-img" role="img" aria-label="Colleagues looking at a presentation chart together" style="background:linear-gradient(135deg,#5a5450,#c8c4bf 50%,#e7eef5)"></div>
    <h3>Bonorum et Malorum</h3>
    <div class="meta"><span>▦ 04/05/2015</span><span>◷ 9.00 am</span><span>◌ 20</span></div>
    <p>Contrary to popular Ipsum simply random ... <span class="more">Read More »</span></p>
  </div>
  <div class="abs card" style="left:543px">
    <div class="card-img" role="img" aria-label="Hands using a tablet beside a laptop keyboard" style="background:linear-gradient(135deg,#2f3440,#6d7a90 50%,#c2cbd8)"></div>
    <h3>Bonorum et Malorum</h3>
    <div class="meta"><span>▦ 04/05/2015</span><span>◷ 9.00 am</span><span>◌ 20</span></div>
    <p>Contrary to popular Ipsum simply random ... <span class="more">Read More »</span></p>
  </div>
  <div class="abs rule" style="top:818px"></div>

  <h2 class="abs ins-h">Larchmere Insurance</h2>
  <p class="abs ins-text">Sed ut perspiciatis unde omnis iste natus error sit voluptatem accusantium doloremque laudantium, totam rem aperiam, eaque ipsa quae ab illo inventore veritatis et quasi architecto beatae vitae dicta sunt explicabo.</p>
  <a class="abs btn ins-btn">Buy Insurance</a>

  <div class="abs quote">
    <div class="quote-h">Request a Quote</div>
    <p>Sed ut perspiciatis unde omnis iste natus error sit voluptatem</p>
    <div class="field">Enter a Email Address</div>
    <a class="btn quote-btn">GET A QUOTE</a>
  </div>

  <footer class="abs footer"></footer>
  <div class="abs col-rule" style="left:167px"></div>
  <div class="abs col-rule" style="left:395px"></div>
  <div class="abs col-rule" style="left:554px"></div>

  <div class="abs f-h" style="left:64px">Links</div>
  <ul class="abs f-list f-links"><li>Fighting for childhood</li><li>Preventing abuse</li><li>Donate</li><li>About us</li></ul>

  <div class="abs f-h" style="left:192px"><span style="width:10px;height:10px;border-radius:50%;background:#2a9fd6;display:inline-block"></span>Latest Tweets</div>
  <div class="abs tweet">
    <div class="abs avatar" role="img" aria-label="Profile photo"></div>
    <p class="abs tw-text"><b>LarchGossip</b> <i>@Larchmere</i><br>UPDATE 1-Veltrano's CEO candidate leaves in surprise move http://wirew.ll/3KQpx via <i>@Wirewell</i></p>
    <div class="abs tw-actions">
      <svg width="10" height="9" viewBox="0 0 10 9"><path d="M4 1 L1 4 L4 7 M1 4 H6 Q9 4 9 8" fill="none" stroke="#555" stroke-width="1.3"/></svg>
      <svg width="11" height="9" viewBox="0 0 11 9"><path d="M2 7 V2 H8 M6 0.5 L8 2 L6 3.5 M9 2 V7 H3 M5 8.5 L3 7 L5 5.5" fill="none" stroke="#555" stroke-width="1.1"/></svg>
      <svg width="10" height="9" viewBox="0 0 10 10"><polygon points="5,0.5 6.3,3.7 9.6,3.8 7,5.9 7.9,9.2 5,7.3 2.1,9.2 3,5.9 0.4,3.8 3.7,3.7" fill="#555"/></svg>
    </div>
    <span class="abs tw-summary">View Summary</span>
  </div>

  <div class="abs f-h" style="left:424px">Related Resources</div>
  <ul class="abs f-list f-res"><li>Pellentesque sed dolor</li><li>Aliquam congue nisl</li><li>Mauris accumsan nulla</li><li>Pellentesque sed dolor</li><li>Aliquam congue fermentum</li><li>Mauris accumsan nulla</li></ul>

  <div class="abs f-h" style="left:579px">Contact Us</div>
  <div class="contact-row" style="top:1038px">
    <svg width="8" height="11" viewBox="0 0 8 11"><path d="M4 11 L0.8 5.5 A3.6 3.6 0 1 1 7.2 5.5 Z" fill="#3f9d2b"/><circle cx="4" cy="3.8" r="1.3" fill="#e8e8e8"/></svg>
    <span class="contact" style="position:static">12 Alderbrook Lane,<br>Fenwick, D04 0000 street</span>
  </div>
  <div class="contact-row" style="top:1070px">
    <svg width="9" height="9" viewBox="0 0 10 10"><path d="M2 0.5 L4 3 L3 4.3 Q4.5 6.5 5.7 7 L7 6 L9.5 8 L8.3 9.5 Q2.5 9 0.5 1.7 Z" fill="#3f9d2b"/></svg>
    <span class="contact" style="position:static">1 555-010-0188 /<br>1 555-010-0142</span>
  </div>
  <div class="contact-row" style="top:1103px">
    <svg width="11" height="8" viewBox="0 0 11 8"><rect width="11" height="8" fill="#3f9d2b"/><polyline points="0.5,0.5 5.5,4.5 10.5,0.5" fill="none" stroke="#e8e8e8" stroke-width="1"/></svg>
    <span class="contact" style="position:static">larchmere @ mail.example</span>
  </div>

  <div class="abs bottom"></div>
  <p class="abs copy">Copyright © 2015 Larchmere / All rights reserved.</p>
  <span class="abs social" style="left:597px"></span>
  <span class="abs social" style="left:623px"></span>
  <span class="abs social" style="left:649px"></span>
</div>
</body>
</html>
```